Vireo M.K. - Diagnostic Ultrasound Flyer

About US
Vireo M.K. is a concierge ultrasound company that provides onsite or offsite diagnostic ultrasounds. We have over 14 years experience in sonography, business management, and customer service. We offer both the physician and patient flexibility, convenience, and access to timely services.

We provide ultrasounds for the following specialties:
Obstetrics/Gynecology
Abdominal
Small Parts
Vascular

Company Features:
1. Onsite or Offsite Scans
2. Images Available Immediately for Referring Physician and Patient
3. Flexible Options for Ultrasound Interpretation/Billing
4. Access to Interpreting Radiologist
5. Final Report Process - 1-2 Business Days/ 1 hour for STAT.
6. PACS Storage with Secure Access.

We need a place to add in our contact information (address, email, website, phone)

We already have a logo and would like to use it ( they are attached). We would the colors to match the logo colors....maybe lighter version of yellow and blue.

```html
<!DOCTYPE html>
<html lang="en">
<head>
<meta charset="utf-8">
<title>Vireo M.K. – Diagnostic Ultrasound Flyer</title>
<link rel="stylesheet" href="https://fonts.googleapis.com/css2?family=Oswald:wght@300;400&family=Roboto+Condensed:wght@400;500&family=Montserrat:wght@800&display=swap">
<style>
  :root {
    --navy: #2b3990;
    --yellow: #f9b934;
    --paper: #ffffff;
    --backdrop: #e4e1e0;
    --photo-light: #e9e6e3;
  }
  * { margin: 0; padding: 0; box-sizing: border-box; }
  html, body { width: 1200px; height: 1200px; overflow: hidden; background: var(--backdrop); }
  .flyer {
    position: absolute; left: 204px; top: 40px;
    width: 450px; height: 636px;
    background: var(--paper);
    transform: scale(1.76); transform-origin: 0 0;
    overflow: hidden;
    font-family: "Roboto Condensed", sans-serif;
    color: var(--navy);
  }
  .flyer-shapes { position: absolute; inset: 0; width: 450px; height: 636px; }
  .brand {
    position: absolute; left: 20px; top: 26px;
    display: flex; align-items: center; gap: 6px;
    font-family: "Montserrat", sans-serif; font-weight: 800;
    font-size: 19px; letter-spacing: 0.5px; color: var(--navy);
  }
  .brand-dot { width: 9px; height: 9px; border-radius: 50%; background: var(--yellow); }
  .heading {
    position: absolute; font-family: "Oswald", sans-serif; font-weight: 300;
    text-transform: uppercase; color: var(--navy); line-height: 1.2;
    white-space: nowrap;
  }
  .about-title { left: 0; width: 232px; top: 115px; text-align: center; font-size: 27px; }
  .about-text {
    position: absolute; left: 11px; top: 159px; width: 214px;
    font-size: 9.3px; line-height: 14.7px; color: var(--navy);
  }
  .specialties-title { left: 130px; width: 295px; top: 328px; text-align: center; font-size: 24px; line-height: 34px; }
  .specialty {
    position: absolute; display: flex; align-items: center; gap: 6px;
    font-size: 17px; line-height: 1; white-space: nowrap;
  }
  .wave { width: 9px; height: 11px; }
  .features-title { left: 130px; top: 460px; font-size: 27px; }
  .features { position: absolute; left: 133px; top: 508px; list-style: none; }
  .features li {
    position: absolute; left: 0; display: flex; align-items: center; gap: 6px;
    white-space: nowrap; font-size: 9.6px;
  }
  .features .num {
    width: 10px; height: 10px; border-radius: 50%; background: var(--yellow);
    color: #fff; font-size: 6.5px; font-weight: 500;
    display: flex; align-items: center; justify-content: center;
  }
  .contact { position: absolute; left: 12px; top: 566px; list-style: none; }
  .contact li {
    display: flex; align-items: center; gap: 6px; white-space: nowrap;
    font-size: 7px; height: 16.3px; color: var(--navy);
  }
  .contact svg { width: 10px; height: 10px; fill: var(--navy); }
</style>
</head>
<body>
<main class="flyer">
  <svg class="flyer-shapes" viewBox="0 0 450 636">
    <defs>
      <linearGradient id="scanPhoto" x1="0" y1="0" x2="1" y2="1">
        <stop offset="0" stop-color="#eeeae6"/>
        <stop offset="0.5" stop-color="#c7cfd8"/>
        <stop offset="1" stop-color="#8b9aa6"/>
      </linearGradient>
      <linearGradient id="bellyPhoto" x1="0" y1="0" x2="0" y2="1">
        <stop offset="0" stop-color="#e9e6e3"/>
        <stop offset="0.5" stop-color="#d8c9bf"/>
        <stop offset="1" stop-color="#e9e6e3"/>
      </linearGradient>
    </defs>
    <polygon points="194,0 450,0 450,245 340,308 215,245 215,80" fill="var(--navy)" stroke="var(--navy)" stroke-width="10" stroke-linejoin="round"/>
    <polygon role="img" aria-label="Photo of a pregnant patient receiving an ultrasound scan"
      points="325,-6 450,58 450,232 328,298 205,232 205,62" fill="url(#scanPhoto)" stroke="url(#scanPhoto)" stroke-width="10" stroke-linejoin="round"/>
    <polygon role="img" aria-label="Photo of hands forming a heart over a pregnant belly"
      points="0,286 117,348 117,498 0,560" fill="url(#bellyPhoto)"/>
    <polygon points="115,70 236,137 236,266 115,330 -6,266 -6,137" fill="var(--yellow)" stroke="var(--yellow)" stroke-width="12" stroke-linejoin="round"/>
    <polygon points="0,552 121,500 121,636 0,636" fill="var(--yellow)"/>
  </svg>

  <div class="brand"><span class="brand-dot"></span>VIREO M.K.</div>

  <h2 class="heading about-title">About Us:</h2>
  <p class="about-text">Vireo M.K. is a concierge ultrasound company that provides onsite or offsite diagnostic ultrasounds. We have over 14 years experience in sonography, business management, and customer service. We offer both the physician and patient flexibility, convenience, and access to timely services.</p>

  <h2 class="heading specialties-title">We provide ultrasounds for<br>the following specialties:</h2>
  <div class="specialty" style="left:132px;top:404px"><svg class="wave" viewBox="0 0 9 11"><path d="M4 1 Q0 5.5 4 10 M8 2.5 Q5.5 5.5 8 8.5" stroke="#f9b934" stroke-width="1.2" fill="none"/></svg>Obstetrics/Gynecology</div>
  <div class="specialty" style="left:132px;top:430px"><svg class="wave" viewBox="0 0 9 11"><path d="M4 1 Q0 5.5 4 10 M8 2.5 Q5.5 5.5 8 8.5" stroke="#f9b934" stroke-width="1.2" fill="none"/></svg>Abdominal</div>
  <div class="specialty" style="left:322px;top:406px"><svg class="wave" viewBox="0 0 9 11"><path d="M4 1 Q0 5.5 4 10 M8 2.5 Q5.5 5.5 8 8.5" stroke="#f9b934" stroke-width="1.2" fill="none"/></svg>Small Parts</div>
  <div class="specialty" style="left:322px;top:432px"><svg class="wave" viewBox="0 0 9 11"><path d="M4 1 Q0 5.5 4 10 M8 2.5 Q5.5 5.5 8 8.5" stroke="#f9b934" stroke-width="1.2" fill="none"/></svg>Vascular</div>

  <h2 class="heading features-title">Company Features:</h2>
  <ol class="features">
    <li style="top:0"><span class="num">1</span>Onsite or Offsite Scans</li>
    <li style="top:17px"><span class="num">2</span>Images Available Immediately for Referring Physician and Patient.</li>
    <li style="top:34px"><span class="num">3</span>Flexible Options for Ultrasound Interpretation/Billing</li>
    <li style="top:55px"><span class="num">4</span>Access to Interpreting Radiologist</li>
    <li style="top:72px"><span class="num">5</span>Final Report Process - 1-2 Business Days/ 1 hour for STAT.</li>
    <li style="top:89px"><span class="num">6</span>PACS Storage with Secure Access.</li>
  </ol>

  <ul class="contact">
    <li><svg viewBox="0 0 10 10"><path d="M5 0 C2.2 0 1 2 1 3.8 C1 6.5 5 10 5 10 C5 10 9 6.5 9 3.8 C9 2 7.8 0 5 0 Z M5 2.3 A1.5 1.5 0 1 1 5 5.3 A1.5 1.5 0 1 1 5 2.3 Z"/></svg>Your Address.</li>
    <li><svg viewBox="0 0 10 10"><path d="M0 2 H10 V8 H0 Z M0.8 2.6 L5 5.6 L9.2 2.6" stroke="#f9b934" stroke-width="0.6"/></svg>hello@vireomk.example</li>
    <li><svg viewBox="0 0 10 10"><circle cx="5" cy="5" r="4.4" fill="none" stroke="#2b3990" stroke-width="0.9"/><path d="M0.6 5 H9.4 M5 0.6 C2.5 3 2.5 7 5 9.4 M5 0.6 C7.5 3 7.5 7 5 9.4" fill="none" stroke="#2b3990" stroke-width="0.7"/></svg>www.vireomk.example</li>
    <li><svg viewBox="0 0 10 10"><path d="M2 0.5 L3.8 2.6 L2.8 3.8 C3.5 5.3 4.7 6.5 6.2 7.2 L7.4 6.2 L9.5 8 L8.2 9.5 C4.3 9.2 0.8 5.7 0.5 1.8 Z"/></svg>000 000 48390</li>
  </ul>
</main>
</body>
</html>
```